business card for LWR pty ltd

We require a business card that stands out . I have included our company flyer and would like the services listed to be put on the card so when we Give out the cards to customers they have an idea of services we provide. need the winning design to be in editable photo shop format, editable iMac pages format or editable windows publisher format, so that I can enter in names, email addresses, phone numbers etc myself. I have included a pdf documents of info / items needed on the card to use as reference please.
Updates

need more submissions

Need extra days to review

Sick

Target Market(s)

new customers

Contact Information for Business Card

details are on attached business card requirements file

Requirements
Must have
• I have attached a list of must haves

```html
<!DOCTYPE html>
<html lang="en">
<head>
<meta charset="utf-8">
<title>LWR Pty Ltd – Business Card</title>
<link href="https://fonts.googleapis.com/css2?family=Open+Sans:ital,wght@0,400;0,600;0,700;0,800;1,400&family=Michroma&display=swap" rel="stylesheet">
<style>
  :root{
    --page:#c9c9c9;
    --card:#ffffff;
    --ink:#1c1c1c;
    --yellow:#f2b01e;
    --steel:#b9bdc2;
    --dark-top:#1a1a1a;
    --dark-mid:#2e2e2e;
    --earth:#8a6a4a;
    --grey-strip:#9a9a9a;
    --rule:#8c8c8c;
  }
  *{margin:0;padding:0;box-sizing:border-box}
  html,body{width:1200px;height:1200px;overflow:hidden}
  body{background:var(--page);font-family:"Open Sans",Arial,sans-serif;color:var(--ink);position:relative}
  .card{position:absolute;left:228px;width:744px;height:456px;background:var(--card);overflow:hidden}
  .card--front{top:96px}
  .card--back{top:648px}
  .card__art{position:absolute;inset:0;width:100%;height:100%}
  .t{position:absolute;line-height:1;white-space:nowrap}
  .brand-mark{font-family:"Open Sans",Arial,sans-serif;font-weight:800;color:var(--steel);letter-spacing:4px}
  .holder-name{font-weight:700;font-size:27px;letter-spacing:.5px}
  .holder-role{font-style:italic;font-size:18px;color:var(--yellow)}
  .company{font-weight:700;font-size:17px}
  .contact{font-size:18px}
  .services-title{font-family:"Michroma",Arial,sans-serif;font-size:21px;letter-spacing:3px;color:#3a3a3a}
  .service{font-size:16px}
  .service::before{content:"";display:inline-block;width:5px;height:5px;border-radius:50%;background:var(--yellow);margin-right:8px;vertical-align:middle;position:relative;top:-2px}
  .service--cont::before{display:none}
  .website{font-weight:700;font-size:25px;color:#fff}
</style>
</head>
<body>

<!-- Front -->
<section class="card card--front">
  <svg class="card__art" viewBox="0 0 496 304" preserveAspectRatio="none">
    <defs>
      <linearGradient id="frontPhoto" x1="0" y1="0" x2="0" y2="1">
        <stop offset="0" stop-color="var(--dark-top)"/>
        <stop offset=".65" stop-color="var(--dark-mid)"/>
        <stop offset="1" stop-color="var(--earth)"/>
      </linearGradient>
      <linearGradient id="frontShade" x1="0" y1="0" x2="1" y2="0">
        <stop offset="0" stop-color="#8f8f8f"/>
        <stop offset="1" stop-color="#f2f2f2"/>
      </linearGradient>
    </defs>
    <polygon points="0,72 178,72 332,304 0,304" fill="url(#frontPhoto)" role="img" aria-label="Photo of a road train tanker truck against a dark metal mesh backdrop"/>
    <polygon points="380,250 496,235 496,304 410,304" fill="url(#frontShade)"/>
    <polygon points="153,35 180,35 412,304 332,304" fill="var(--yellow)"/>
    <line x1="248" y1="88" x2="412" y2="88" stroke="var(--yellow)" stroke-width="1.3"/>
    <!-- phone -->
    <g transform="translate(268,150)" fill="var(--ink)">
      <path d="M-3,-4 q-1,0 -1,1.5 q0.5,4 5,6.5 q1.5,0.5 2,-0.5 l0.5,-1 l-2,-1.5 l-1,1 q-2,-1 -3,-3 l1,-1 l-1.5,-2 z"/>
    </g>
    <!-- mail -->
    <g transform="translate(280,169)" fill="none" stroke="var(--ink)" stroke-width="1">
      <rect x="-4" y="-3" width="8" height="6"/>
      <polyline points="-4,-3 0,0.5 4,-3"/>
    </g>
    <!-- pin -->
    <g transform="translate(291,189)" fill="var(--ink)">
      <path d="M0,5 L-3.2,-0.5 A3.7,3.7 0 1 1 3.2,-0.5 Z"/>
      <circle cx="0" cy="-2" r="1.3" fill="#fff"/>
    </g>
  </svg>

  <div class="t brand-mark" style="left:38px;top:160px;font-size:76px">LWR</div>

  <div class="t holder-name" style="left:375px;top:98px">DANIEL HART</div>
  <div class="t holder-role" style="left:398px;top:136px">Director</div>
  <div class="t company" style="left:438px;top:185px">LWR Pty Ltd</div>
  <div class="t contact" style="left:458px;top:215px">000 444 000</div>
  <div class="t contact" style="left:477px;top:244px">email@lwrservices.com.au</div>
  <div class="t contact" style="left:502px;top:273px">Depot: Lot 444</div>
  <div class="t contact" style="left:518px;top:301px">example address Australia</div>
</section>

<!-- Back -->
<section class="card card--back">
  <svg class="card__art" viewBox="0 0 496 304" preserveAspectRatio="none">
    <defs>
      <linearGradient id="backPhoto" x1="0" y1="0" x2="0" y2="1">
        <stop offset="0" stop-color="var(--dark-top)"/>
        <stop offset=".6" stop-color="var(--dark-mid)"/>
        <stop offset="1" stop-color="var(--earth)"/>
      </linearGradient>
      <linearGradient id="webStrip" x1="0" y1="0" x2="1" y2="0">
        <stop offset="0" stop-color="#6f6f6f"/>
        <stop offset="1" stop-color="#d6d6d6"/>
      </linearGradient>
    </defs>
    <polygon points="0,0 130,0 318,304 0,304" fill="url(#backPhoto)" role="img" aria-label="Photo of two road train prime movers against a dark metal mesh backdrop"/>
    <polygon points="270,262 496,262 496,304 296,304" fill="url(#webStrip)"/>
    <polygon points="130,0 160,0 362,252 300,280" fill="var(--yellow)"/>
    <line x1="200" y1="41" x2="376" y2="41" stroke="var(--rule)" stroke-width="1"/>
    <circle cx="287" cy="282" r="5" fill="var(--yellow)"/>
  </svg>

  <div class="t brand-mark" style="left:38px;top:102px;font-size:70px">LWR</div>

  <div class="t services-title" style="left:318px;top:30px">OUR SERVICES</div>

  <div class="t service" style="left:348px;top:76px">Over size loads / Hot Shot Loads</div>
  <div class="t service" style="left:363px;top:98px">Heavy Vehicle Recovery services</div>
  <div class="t service" style="left:378px;top:120px">Potable Water Deliveries</div>
  <div class="t service" style="left:393px;top:142px">Road Building / Maintenance</div>
  <div class="t service" style="left:408px;top:164px">Earthworks</div>
  <div class="t service" style="left:423px;top:186px">Sand &amp; Metal Supply &amp; Cartage</div>
  <div class="t service" style="left:438px;top:208px">Road Train Tippers</div>
  <div class="t service" style="left:453px;top:230px">Road Train Tankers</div>
  <div class="t service" style="left:468px;top:252px">Road Train Flat Tops</div>
  <div class="t service" style="left:483px;top:274px">Drop Deck Trailers</div>
  <div class="t service" style="left:498px;top:296px">Mine site accredited</div>
  <div class="t service service--cont" style="left:528px;top:318px">equipment &amp; Operators</div>

  <div class="t website" style="left:450px;top:410px">www.website.com</div>
</section>

</body>
</html>
```